Web Design Project for selling festive lights

I need a modern and easy to navigate website that is going to sell festive lights.
The name of the site will be "wrenglow" and the logo can be found in the following link: http://qv.zx/Tr8peWm3?
The target group will be people that search for nice decoration lights for their living room, patio and children bedroom.
We need to have a professional look in order to make our webpage distinctive among competition.
The actual products that we are going to sell are cotton ball lights. Pictures can be found in websites like threadandlamp.co.uk and many others.
I need to have a design of the homepage, products pages, customer review page, and shopping cart. The design will be "locked" on a php.

Requirements
Must have
• The fonts used in the design must be compatible with the Greek language because that site will be in Greek.
Nice to have
• Flash and non flash banners

```html
<!DOCTYPE html>
<html lang="en">
<head>
<meta charset="utf-8">
<title>wrenglow – Cotton Ball Lights</title>
<link rel="stylesheet" href="https://fonts.googleapis.com/css2?family=Arimo:wght@400;700&display=swap">
<style>
  :root {
    --band-grey: #d9d9d9;
    --band-grey-light: #e4e4e4;
    --footer-grey: #e2e2e2;
    --white: #ffffff;
    --ink: #1f1f1f;
    --ink-soft: #444444;
    --rule: #c4c4c4;
    --yellow: #fbd730;
    --button-grey: #8e8e8e;
    --tab-grey: #a9a9a9;
    --photo-brown: #4a3a30;
    --brand-bg: #f2f2f2;
  }
  * { box-sizing: border-box; margin: 0; padding: 0; }
  html, body { width: 1109px; height: 1200px; overflow: hidden; }
  body {
    position: relative;
    font-family: "Arimo", Arial, sans-serif;
    color: var(--ink);
    background: var(--white);
  }
  .top-band {
    position: absolute; left: 0; top: 0; width: 1109px; height: 396px;
    background: radial-gradient(circle at 30% 20%, var(--band-grey-light), var(--band-grey) 70%);
  }
  .footer-band {
    position: absolute; left: 0; top: 934px; width: 1109px; height: 266px;
    background: var(--footer-grey);
  }

  /* Header */
  .brand {
    position: absolute; left: 42px; top: 0; width: 190px; height: 120px;
    border: 1px solid #b8b8b8; border-top: none;
    background: var(--brand-bg);
    display: flex; align-items: center; justify-content: center; gap: 8px;
  }
  .brand-dot { width: 12px; height: 12px; border-radius: 50%; background: var(--yellow); }
  .brand-name { font-size: 24px; font-weight: 700; color: #3a3a3a; }

  .utility {
    position: absolute; top: 0; left: 848px; height: 27px;
    display: flex; align-items: center; font-size: 11px; color: var(--ink);
  }
  .social { display: flex; gap: 6px; margin-right: 14px; }
  .social span { width: 20px; height: 20px; border-radius: 3px; background: #6f8fb8; display: block; }
  .languages {
    display: flex; align-items: center; gap: 6px; height: 27px; padding: 0 8px;
    border-left: 1px solid #b5b5b5; border-right: 1px solid #b5b5b5;
    background: var(--band-grey-light);
  }
  .flag { width: 18px; height: 11px; display: inline-block; background: #6a7fb0; margin-right: 4px; vertical-align: -1px; }
  .languages .sep { color: #777; }

  .main-nav {
    position: absolute; top: 88px; left: 518px; height: 34px;
    display: flex; font-size: 15px;
  }
  .main-nav a {
    color: var(--ink); text-decoration: none; height: 34px; line-height: 34px;
    text-align: center;
  }
  .main-nav .is-active {
    width: 92px; color: var(--white); border-radius: 4px 4px 0 0;
    background: linear-gradient(var(--tab-grey), #c8c8c8);
    border: 1px solid #999; border-bottom: none;
  }
  .main-nav .about { width: 118px; }
  .main-nav .products { width: 110px; }
  .main-nav .store { width: 96px; }
  .main-nav .contact { width: 122px; }

  /* Hero */
  .hero {
    position: absolute; left: 42px; top: 120px; width: 1022px; height: 440px;
    background: var(--white); padding: 5px;
  }
  .hero-visual {
    width: 100%; height: 100%;
    background: radial-gradient(circle at 65% 55%, #b05a52 0, #7a4a3e 25%, var(--photo-brown) 60%, #2e241e 100%);
  }

  /* Products */
  .section-title { position: absolute; font-size: 24px; font-weight: 400; color: var(--ink); }
  .products-title { left: 43px; top: 580px; }
  .products-rule { position: absolute; left: 42px; top: 612px; width: 1022px; height: 1px; background: var(--rule); }

  .carousel-arrow { position: absolute; top: 734px; width: 18px; height: 30px; }
  .carousel-arrow.prev { left: 50px; }
  .carousel-arrow.next { left: 1036px; }

  .product-card { position: absolute; top: 636px; width: 208px; }
  .product-frame {
    width: 202px; height: 222px; background: var(--white); padding: 5px;
    border-radius: 4px; box-shadow: 0 0 4px rgba(0,0,0,.35);
  }
  .product-visual { width: 100%; height: 100%; }
  .product-price {
    position: relative; margin-top: 9px; width: 204px; height: 33px;
    background: var(--yellow); border-radius: 5px 0 0 5px;
    font-size: 17px; line-height: 34px; padding-left: 14px; color: var(--ink);
  }
  .price-go {
    position: absolute; right: -4px; top: -4px; width: 41px; height: 41px;
    border-radius: 50%; background: var(--button-grey); border: 3px solid var(--white);
    box-shadow: 0 0 2px rgba(0,0,0,.4);
  }
  .price-go svg { position: absolute; left: 11px; top: 8px; }

  /* About & newsletter */
  .about-title { left: 43px; top: 958px; }
  .about-copy {
    position: absolute; left: 43px; top: 990px; width: 705px;
    font-size: 13.3px; line-height: 19px; letter-spacing: .2px; color: var(--ink);
    text-align: justify;
  }
  .read-more { position: absolute; left: 685px; top: 1100px; font-size: 10px; color: var(--ink-soft); text-decoration: none; }

  .newsletter-title { left: 782px; top: 958px; letter-spacing: .5px; }
  .newsletter-box {
    position: absolute; left: 772px; top: 994px; width: 287px; height: 112px;
    background: var(--white); border-radius: 3px; padding: 5px;
    box-shadow: 0 0 4px rgba(0,0,0,.25);
  }
  .newsletter-inner { width: 100%; height: 100%; border: 1px solid #d0d0d0; position: relative; }
  .email-field {
    position: absolute; left: 18px; top: 25px; width: 248px; height: 30px;
    border: 1px solid #bdbdbd; background: var(--white);
  }
  .email-label { position: absolute; left: 19px; top: 73px; font-size: 14px; color: var(--ink-soft); }
  .go-button {
    position: absolute; left: 206px; top: 68px; width: 53px; height: 26px;
    background: var(--yellow); border-radius: 5px; border: none;
    font-family: "Arimo", Arial, sans-serif; font-size: 17px; color: var(--ink);
  }

  .footer-rule { position: absolute; left: 42px; top: 1140px; width: 1022px; height: 1px; background: var(--rule); }
  .legal { position: absolute; left: 0; top: 1165px; width: 1109px; text-align: center; font-size: 10.5px; color: var(--ink); }
</style>
</head>
<body>
  <div class="top-band"></div>
  <div class="footer-band"></div>

  <header>
    <div class="brand">
      <span class="brand-dot"></span>
      <span class="brand-name">wrenglow</span>
    </div>

    <div class="utility">
      <div class="social"><span></span><span></span></div>
      <div class="languages">
        <span><i class="flag"></i>English</span>
        <span class="sep">|</span>
        <span><i class="flag"></i>Greek</span>
      </div>
    </div>

    <nav class="main-nav">
      <a class="is-active" href="#">Home</a>
      <a class="about" href="#">About us</a>
      <a class="products" href="#">Products</a>
      <a class="store" href="#">Store</a>
      <a class="contact" href="#">Contact us</a>
    </nav>
  </header>

  <section class="hero">
    <div class="hero-visual" role="img" aria-label="Banner photo of glowing coloured cotton ball lights strung across a dark wooden room"></div>
  </section>

  <h2 class="section-title products-title">Products</h2>
  <div class="products-rule"></div>

  <svg class="carousel-arrow prev" viewBox="0 0 18 30"><polygon points="17,0 17,30 0,15" fill="#9a9a9a"/></svg>
  <svg class="carousel-arrow next" viewBox="0 0 18 30"><polygon points="1,0 1,30 18,15" fill="#9a9a9a"/></svg>

  <article class="product-card" style="left:82px">
    <div class="product-frame"><div class="product-visual" role="img" aria-label="Photo of a black and a pale cotton ball light" style="background:linear-gradient(160deg,#1b1b1b 0,#3a3a36 35%,#cfcfbf 55%,#5a5650 100%)"></div></div>
    <div class="product-price">£23.95<span class="price-go"><svg width="18" height="20" viewBox="0 0 18 20"><polygon points="0,0 18,10 0,20" fill="#fff"/></svg></span></div>
  </article>

  <article class="product-card" style="left:331px">
    <div class="product-frame"><div class="product-visual" role="img" aria-label="Photo of warm beige cotton ball lights glowing" style="background:radial-gradient(circle at 60% 50%,#f1deb0 0,#c9b48c 50%,#4a3b2a 100%)"></div></div>
    <div class="product-price">£23.95<span class="price-go"><svg width="18" height="20" viewBox="0 0 18 20"><polygon points="0,0 18,10 0,20" fill="#fff"/></svg></span></div>
  </article>

  <article class="product-card" style="left:574px">
    <div class="product-frame"><div class="product-visual" role="img" aria-label="Photo of a purple and a teal cotton ball light" style="background:linear-gradient(110deg,#b58ad8 0,#8c5fb8 35%,#3f9a8c 55%,#2b6f66 100%)"></div></div>
    <div class="product-price">£23.95<span class="price-go"><svg width="18" height="20" viewBox="0 0 18 20"><polygon points="0,0 18,10 0,20" fill="#fff"/></svg></span></div>
  </article>

  <article class="product-card" style="left:819px">
    <div class="product-frame"><div class="product-visual" role="img" aria-label="Photo of a string of grey and cream cotton ball lights on black" style="background:radial-gradient(ellipse 30% 60% at 50% 50%,#c8bfae 0,#7a7368 55%,#141414 100%)"></div></div>
    <div class="product-price">£23.95<span class="price-go"><svg width="18" height="20" viewBox="0 0 18 20"><polygon points="0,0 18,10 0,20" fill="#fff"/></svg></span></div>
  </article>

  <h2 class="section-title about-title">About us</h2>
  <p class="about-copy">Lorem Ipsum is simply dummy text of the printing and typesetting industry. Lorem Ipsum has been the industry's standard dummy text ever since the 1500s, when an unknown printer took a galley of type and scrambled it to make a type specimen book. It has survived not only five centuries, but also the leap into electronic typesetting, remaining essentially unchanged. It was popularised in the 1960s with the release of Lettrafold sheets containing Lorem Ipsum passages, and more recently with desktop publishing software like Aldrin PageForge including versions of Lorem Ipsum.</p>
  <a class="read-more" href="#">Read More</a>

  <h2 class="section-title newsletter-title">Newsletter Sign up</h2>
  <div class="newsletter-box">
    <div class="newsletter-inner">
      <div class="email-field"></div>
      <span class="email-label">Enter your email ID</span>
      <button class="go-button">Go</button>
    </div>
  </div>

  <div class="footer-rule"></div>
  <p class="legal">© 2012 wrenglow - Terms of Service - Privacy Policy - Program Policies</p>
</body>
</html>
```